Starter & Alternator business needs a website

update: very good designs submitted so far. also need this to display well on mobile devices. not sure if wordpress or html/css is better for my needs.

Our existing website is vexlandrib.com and is need of total revamp. Need full design of a website for my business.

We sell and rebuild starters and alternators. Customers bring in the units and we rebuild them. Or we sell them brand new or rebuilt units we have in stock. We do not install units into vehicles like a mechanic would. We strictly rebuild starters and alternators in our shop, sell brand new units over the counter, and we do deliver occasionally as well. We do offer a line of Morlin batteries as well but that is only a small feature of the business.

I would like this website designed and coded. I can upload the files to my web host after completion. I can also add in and modify content like our background info, etc.

I have included an illustrator file that shows some of our signage and logo, etc. I have also included a radio commercial sample so you can get a little better feel for the business. A similar ad does run on the radio currently, slightly different and without the added sound effects.

Update: I do like using photos of real items(starters or alternators etc) for an icon, like a real alternator stock image for the alternator section icon, etc. Maybe incorporate our logo in that design as well. That looks nice as well and may aid in navigation.

For any other design elements, do what you think looks good. Our colors are red/white/blue as seen in the illustrator file. our building is painted with talbot greaves colors, emberglow red and deep harbor for blue.

Here are some examples of rebuilders websites in other markets for reference:

https://brommelgarage.com/starter-alternator-rebuilding/

https://www.quintonmotorworks.com/auto-repairs/alternator-starter-rebuilds.aspx

https://www.lorvexcharging.com/

https://www.damblingwx.com/

The website can have areas for: services and products offered, high output alternators, Morlin Batteries, troubleshooting tips, current specials, contact info and directions/map, etc. Whatever else you feel applies.

At some point I do want to be able to sell items directly online or at least have a secure section for customers to submit invoice payments, but that's not necessarily in scope for this project just something to keep in mind.

Target Market(s)

Mechanics and Managers in fleet shops, construction and marine industries, shipping trades. Also automobile owners who work on their own vehicles. We sell and rebuild starters and alternators for automobiles, heavy duty equipment, forklifts, gradalls, man movers, bobcats, loaders, large tractors and trucks, just about any engine, golf carts, generators, etc.

Industry/Entity Type

Automotive Part

Coding

Coded - Design and coding required

Number of Pages Required

5+ page

Font styles to use
Serif
Sans Serif

Colors
0255a3
ec1f27
ffffff

Requirements
Must have
• Should also display nicely on mobile phones. Highlight our specialty, "Starters & Alternators"

```html
<!DOCTYPE html>
<html lang="en">
<head>
<meta charset="utf-8">
<title>Harbor Coil Rebuilders – Troubleshooting Tips</title>
<link href="https://fonts.googleapis.com/css2?family=Jost:wght@400;500;700&family=Libre+Baskerville:wght@700&display=swap" rel="stylesheet">
<style>
:root{
  --red:#a80000;
  --navy:#0c1142;
  --hero:#24344f;
  --ink:#222;
  --muted:#444;
  --line:#ddd;
  --crumb:#f3f3f3;
  --white:#fff;
}
*{box-sizing:border-box;margin:0;padding:0}
html,body{width:695px;height:1200px;overflow:hidden;background:var(--white)}
body{position:relative;font-family:"Jost",sans-serif;color:var(--ink)}
.abs{position:absolute}
.serif{font-family:"Libre Baskerville",serif}

/* hero */
.hero{left:0;top:0;width:695px;height:238px;background:radial-gradient(ellipse at 30% 55%,#4b5a74 0%,#2a3a56 45%,#1a2740 100%)}
.topbar{top:12px;font-size:10px;color:var(--white)}
.address{left:93px}
.phone-top{left:490px;width:112px;display:flex;align-items:center;gap:5px}
.phone-top i{flex:1;height:1px;background:var(--white)}
.navband{left:0;top:38px;width:695px;height:29px;background:var(--red)}
.nav{top:46px;font-size:9px;color:var(--white);display:flex;gap:10px}
.nav-left{left:93px}
.nav-right{left:408px}
.brand-badge{left:303px;top:8px;width:88px;height:88px;border-radius:50%;background:var(--white);display:flex;align-items:center;justify-content:center;text-align:center}
.brand-badge span{font-family:"Jost",sans-serif;font-weight:700;font-size:10px;color:var(--navy);line-height:1.2}
.hero-title{left:0;width:695px;top:135px;text-align:center;color:var(--white);font-size:21px}
.hero-sub{left:0;width:695px;top:172px;text-align:center;color:var(--white);font-size:15px;display:flex;justify-content:center;align-items:center;gap:8px}
.hero-sub b{display:inline-block;width:5px;height:14px;background:#d0161d;transform:skewX(-20deg)}

/* breadcrumb */
.crumbs{left:0;top:238px;width:695px;height:22px;background:var(--crumb);font-size:7px;display:flex;align-items:center;padding-left:94px;gap:8px}
.crumbs .here{color:var(--red)}

/* heading */
.page-title{left:0;width:695px;top:283px;text-align:center;font-size:17px;color:var(--ink)}
.page-rule{left:336px;top:310px;width:24px;height:1px;background:#888}

/* cards */
.card{width:159px;height:208px;border:1px solid var(--line);background:var(--white)}
.card .photo{position:absolute;left:0;top:0;width:157px;height:113px}
.card .frame{position:absolute;left:8px;top:8px;right:8px;bottom:0;border:1px solid var(--white);border-bottom:none}
.card .date{position:absolute;left:50%;top:106px;transform:translateX(-50%);background:var(--white);font-size:5.5px;padding:1px 5px;white-space:nowrap}
.card h3{position:absolute;top:128px;left:0;width:100%;text-align:center;font-size:8px;letter-spacing:.3px}
.card p{position:absolute;top:144px;left:0;width:100%;text-align:center;font-size:7.5px;line-height:11px;color:var(--muted)}
.btn{background:var(--red);color:var(--white);text-align:center}
.card .btn{position:absolute;left:50px;top:176px;width:58px;height:17px;font-size:7px;line-height:17px}
.p1{background:linear-gradient(135deg,#3a3a3a,#a9a9a9 45%,#555)}
.p2{background:linear-gradient(180deg,#b9c3c7 0%,#a9b3b7 60%,#8d969b 100%)}
.p3{background:linear-gradient(135deg,#35402a,#a7a28a 50%,#4a4a40)}
.p4{background:linear-gradient(135deg,#222,#777 50%,#3a2a2a)}
.p5{background:linear-gradient(180deg,#f4f6fb,#c8cedb 55%,#3b4052)}
.p6{background:linear-gradient(135deg,#1c1c1c,#9a9a9a 45%,#2a2a2a)}

/* categories */
.cats{left:443px;top:325px;width:159px;height:220px;background:linear-gradient(125deg,var(--navy) 55%,#1c2258 56%,var(--navy) 80%)}
.cats h2{position:absolute;left:17px;top:15px;color:var(--white);font-size:12.5px}
.cats .rule{position:absolute;left:17px;top:36px;width:26px;height:1px;background:var(--white)}
.cats ul{position:absolute;left:16px;top:44px;width:126px;list-style:none}
.cats li{height:21.7px;display:flex;justify-content:space-between;align-items:center;color:var(--white);font-size:8px;border-bottom:1px solid #3a3f6a}
.cats li:last-child{border-bottom:none}
.cats li span:first-child::before{content:"";display:inline-block;width:4px;height:4px;border-radius:50%;background:var(--white);margin-right:4px;vertical-align:1px}

.load-more{left:217px;top:987px;width:87px;height:26px;font-size:9px;line-height:26px}

/* footer */
.foot-rule{left:93px;top:1040px;width:509px;height:1px;background:var(--line)}
.foot-brand{left:93px;top:1066px;width:110px;text-align:center}
.foot-brand .dot{width:36px;height:36px;border-radius:50%;border:3px solid var(--navy);margin:0 auto 6px}
.foot-brand .name{font-weight:700;font-size:13px;line-height:14px;color:var(--navy)}
.foot-brand .tel{margin-top:6px;font-weight:700;font-size:15px;color:var(--red)}
.foot-col h4{font-size:11px;color:var(--navy);margin-bottom:12px}
.foot-col{font-size:9px;color:var(--ink)}
.foot-col li{list-style:none;height:18px}
.company{left:233px;top:1064px}
.location{left:345px;top:1064px}
.location .row{display:flex;gap:6px;line-height:14px;margin-bottom:14px}
.directions{left:473px;top:1064px;width:135px;line-height:14px}
</style>
</head>
<body>

<header>
  <div class="abs hero" role="img" aria-label="Dark blue-tinted photo of alternator and starter parts"></div>
  <div class="abs topbar address">1630 Kelmont Ave</div>
  <div class="abs topbar phone-top"><i></i>555-0142<i></i></div>
  <div class="abs navband"></div>
  <nav class="abs nav nav-left"><span>Home</span><span>Services &amp; Products</span><span>Troubleshooting Tips</span></nav>
  <nav class="abs nav nav-right"><span>Contact Us</span><span>Location &amp; Directions</span></nav>
  <div class="abs brand-badge"><span>Harbor Coil<br>Rebuilders</span></div>
  <h1 class="abs hero-title serif">Starters &amp; Alternators</h1>
  <div class="abs hero-sub serif">Automotive <b></b> Marine <b></b> Heavy Duty</div>
</header>

<div class="abs crumbs"><span>Home</span><span>&#9656;</span><span class="here">Troubleshooting Tips</span></div>

<h2 class="abs page-title serif">TROUBLESHOOTING TIPS</h2>
<div class="abs page-rule"></div>

<article class="abs card" style="left:93px;top:325px">
  <div class="photo p1" role="img" aria-label="Alternator mounted on an engine"><div class="frame"></div></div>
  <span class="date">25 June, 2019</span>
  <h3 class="serif">LOREM IPSUM TEXT OF THE</h3>
  <p>At vero eos et accusamus et ius<br>to odio dignissimos ducimus</p>
  <div class="btn">READ MORE</div>
</article>
<article class="abs card" style="left:268px;top:325px">
  <div class="photo p2" role="img" aria-label="Two alternators on a workbench"><div class="frame"></div></div>
  <span class="date">25 June, 2019</span>
  <h3 class="serif">LOREM IPSUM TEXT OF THE</h3>
  <p>At vero eos et accusamus et ius<br>to odio dignissimos ducimus</p>
  <div class="btn">READ MORE</div>
</article>
<article class="abs card" style="left:93px;top:546px">
  <div class="photo p3" role="img" aria-label="Engine block with belts and pulleys"><div class="frame"></div></div>
  <span class="date">25 June, 2019</span>
  <h3 class="serif">LOREM IPSUM TEXT OF THE</h3>
  <p>At vero eos et accusamus et ius<br>to odio dignissimos ducimus</p>
  <div class="btn">READ MORE</div>
</article>
<article class="abs card" style="left:268px;top:546px">
  <div class="photo p4" role="img" aria-label="Engine bay with distributor and wiring"><div class="frame"></div></div>
  <span class="date">25 June, 2019</span>
  <h3 class="serif">LOREM IPSUM TEXT OF THE</h3>
  <p>At vero eos et accusamus et ius<br>to odio dignissimos ducimus</p>
  <div class="btn">READ MORE</div>
</article>
<article class="abs card" style="left:93px;top:767px">
  <div class="photo p5" role="img" aria-label="Close-up of a machined engine part"><div class="frame"></div></div>
  <span class="date">25 June, 2019</span>
  <h3 class="serif">LOREM IPSUM TEXT OF THE</h3>
  <p>At vero eos et accusamus et ius<br>to odio dignissimos ducimus</p>
  <div class="btn">READ MORE</div>
</article>
<article class="abs card" style="left:268px;top:767px">
  <div class="photo p6" role="img" aria-label="Black and white engine with alternator and pulleys"><div class="frame"></div></div>
  <span class="date">25 June, 2019</span>
  <h3 class="serif">LOREM IPSUM TEXT OF THE</h3>
  <p>At vero eos et accusamus et ius<br>to odio dignissimos ducimus</p>
  <div class="btn">READ MORE</div>
</article>

<aside class="abs cats">
  <h2 class="serif">CATEGORIES</h2>
  <div class="rule"></div>
  <ul>
    <li><span>Lorem Ipsum is simply</span><span>(05)</span></li>
    <li><span>Lorem Ipsum is simply</span><span>(15)</span></li>
    <li><span>Lorem Ipsum is simply</span><span>(08)</span></li>
    <li><span>Lorem Ipsum is simply</span><span>(02)</span></li>
    <li><span>Lorem Ipsum is simply</span><span>(20)</span></li>
    <li><span>Lorem Ipsum is simply</span><span>(36)</span></li>
    <li><span>Lorem Ipsum is simply</span><span>(07)</span></li>
    <li><span>Lorem Ipsum is simply</span><span>(32)</span></li>
  </ul>
</aside>

<div class="abs btn load-more">LOAD MORE</div>

<footer>
  <div class="abs foot-rule"></div>
  <div class="abs foot-brand">
    <div class="dot"></div>
    <div class="name">HARBOR COIL<br>REBUILDERS</div>
    <div class="tel">— 555-0142 —</div>
  </div>
  <div class="abs foot-col company">
    <h4 class="serif">COMPANY</h4>
    <ul><li>Home</li><li>Services &amp; Products</li><li>Troubleshooting Tips</li><li>Contact us</li><li>Location &amp; Directions</li></ul>
  </div>
  <div class="abs foot-col location">
    <h4 class="serif">LOCATION</h4>
    <div class="row">
      <svg width="8" height="10" viewBox="0 0 8 10"><path d="M4 0a4 4 0 0 0-4 4c0 3 4 6 4 6s4-3 4-6a4 4 0 0 0-4-4z" fill="#222"/><circle cx="4" cy="4" r="1.5" fill="#fff"/></svg>
      <span>1630 Kelmont Ave<br>Honolulu, HI 96890</span>
    </div>
    <div class="row">
      <svg width="9" height="9" viewBox="0 0 24 24"><path d="M6.6 10.8a15 15 0 0 0 6.6 6.6l2.2-2.2c.3-.3.7-.4 1-.2 1.1.4 2.3.6 3.6.6.6 0 1 .4 1 1V20c0 .6-.4 1-1 1A17 17 0 0 1 3 4c0-.6.4-1 1-1h3.5c.6 0 1 .4 1 1 0 1.3.2 2.5.6 3.6.1.3 0 .7-.2 1z" fill="#222"/></svg>
      <span>808-555-0143</span>
    </div>
  </div>
  <div class="abs foot-col directions">
    <h4 class="serif">DIRECTIONS</h4>
    We are located 2 blocks Diamond Head of KTC on the Mauka Side of the corner at Kelmont and Ralvo
  </div>
</footer>

</body>
</html>
```